Master / Title Page for Event Planner Proposal

We design our proposals in Publisher. Attached is our current title page and inside pages. We are looking to update our template to something that is classy yet fun. We plan corporate picnics and holiday parties. Please see attached sample of past proposals. The inside pages need to have a design that is very flexible with the number of images used on the page. The image(s) on the cover page would not change. The cover page can have have many images or just one - whichever is best.

```html
<!DOCTYPE html>
<html lang="en">
<head>
<meta charset="utf-8">
<title>Company Picnic 2020 – Event Estimate</title>
<link rel="stylesheet" href="https://fonts.googleapis.com/css2?family=Montserrat:wght@300;400;500;600;700;800&display=swap">
<style>
  :root {
    --backdrop: #cbcbcb;
    --paper: #ffffff;
    --navy: #1f3b78;
    --ink-heading: #1b4a85;
    --ink-body: #2a2a3a;
    --accent-orange: #f7941d;
    --panel-blue: #2e3192;
    --wash-lavender: rgba(120, 110, 200, 0.10);
    --wash-navy: rgba(46, 49, 146, 0.08);
  }
  * { margin: 0; padding: 0; box-sizing: border-box; }
  html, body { width: 1200px; height: 1200px; overflow: hidden; }
  body {
    background: var(--backdrop);
    font-family: "Montserrat", sans-serif;
    position: relative;
  }

  .page {
    position: absolute;
    left: 268px;
    width: 664px;
    height: 464px;
    background: var(--paper);
    overflow: hidden;
  }
  .page--cover { top: 108px; }
  .page--service { top: 628px; }

  /* Cover */
  .cover-decor {
    position: absolute;
    inset: 0;
    background:
      radial-gradient(ellipse 260px 140px at 50% 0%, var(--wash-navy), transparent),
      radial-gradient(ellipse 240px 160px at 50% 100%, var(--wash-navy), transparent),
      radial-gradient(ellipse 160px 220px at 0% 45%, var(--wash-lavender), transparent),
      radial-gradient(ellipse 160px 220px at 100% 55%, var(--wash-lavender), transparent);
  }

  .brand {
    position: absolute;
    left: 88px;
    top: 112px;
    display: flex;
    align-items: center;
    gap: 10px;
  }
  .brand__mark {
    width: 28px; height: 28px;
    border-radius: 50%;
    background: var(--accent-orange);
  }
  .brand__name {
    color: var(--navy);
    font-weight: 700;
    font-size: 19px;
    line-height: 1.15;
    letter-spacing: 0.5px;
    text-transform: uppercase;
  }

  .title-rule {
    position: absolute;
    left: 373px; top: 105px;
    width: 1.5px; height: 52px;
    background: var(--navy);
  }
  .event-title {
    position: absolute;
    left: 397px; top: 114px;
    color: var(--navy);
    font-size: 14.5px;
    line-height: 17px;
    letter-spacing: 0.3px;
  }
  .event-title__name { font-weight: 600; }
  .event-title__kind { font-weight: 400; }

  .details-rule {
    position: absolute;
    left: 330px; top: 204px;
    width: 1.5px; height: 138px;
    background: var(--navy);
  }
  .detail {
    position: absolute;
    color: var(--navy);
  }
  .detail__label {
    font-size: 14.5px;
    font-weight: 400;
    letter-spacing: 0.3px;
    display: flex;
    align-items: center;
    gap: 5px;
  }
  .detail__label::before {
    content: "";
    width: 2px; height: 11px;
    background: var(--accent-orange);
  }
  .detail__value {
    font-size: 14.5px;
    font-weight: 600;
    letter-spacing: 0.3px;
    margin-top: 3px;
    padding-left: 7px;
  }

  /* Service page */
  .service-copy {
    position: absolute;
    left: 46px; top: 62px;
    width: 263px;
    color: var(--ink-body);
  }
  .service-copy__heading {
    color: var(--ink-heading);
    font-weight: 800;
    font-size: 21.5px;
    line-height: 25px;
    letter-spacing: 0.4px;
  }
  .service-copy__lead {
    margin-top: 18px;
    font-size: 14.5px;
    line-height: 17px;
    font-weight: 400;
  }
  .service-copy__lead strong { font-weight: 700; }
  .service-copy__body {
    margin-top: 10px;
    font-size: 10.2px;
    line-height: 12.3px;
    text-align: justify;
    font-weight: 400;
  }
  .service-copy__subheading {
    margin-top: 22px;
    font-size: 14px;
    font-weight: 700;
  }
  .service-copy__body--expect { margin-top: 10px; }
  .service-copy__web {
    position: absolute;
    left: 46px; top: 416px;
    font-size: 9px;
    color: var(--ink-heading);
  }

  .service-panel {
    position: absolute;
    left: 340px; top: 0;
    width: 324px; height: 464px;
    background: var(--panel-blue);
  }
  .service-panel__art {
    position: absolute;
    left: 32px; top: 65px;
    width: 260px; height: 363px;
    border-radius: 8px;
    background: linear-gradient(160deg, #f6a33a 0%, #7b8fe0 50%, #5ec0c8 100%);
    opacity: 0.85;
  }
</style>
</head>
<body>

<section class="page page--cover">
  <div class="cover-decor" role="img" aria-label="Decorative scattered navy, gold and pearl spheres with faint dotted patterns"></div>

  <div class="brand">
    <span class="brand__mark"></span>
    <span class="brand__name">Brightfield<br>Biosciences</span>
  </div>
  <div class="title-rule"></div>
  <div class="event-title">
    <div class="event-title__name">COMPANY PICNIC 2020</div>
    <div class="event-title__kind">EVENT ESTIMATE</div>
  </div>

  <div class="details-rule"></div>
  <div class="detail" style="left:79px;top:201px">
    <div class="detail__label">EVENT DATE:</div>
    <div class="detail__value">SUNDAY &nbsp;|&nbsp; 19 APRIL 2020</div>
  </div>
  <div class="detail" style="left:79px;top:257px">
    <div class="detail__label">EVENT TIME:</div>
    <div class="detail__value">12:00 PM TO 3:00 PM</div>
  </div>
  <div class="detail" style="left:79px;top:310px">
    <div class="detail__label">EVENT LOCATION:</div>
    <div class="detail__value">ON SITE</div>
  </div>
  <div class="detail" style="left:368px;top:201px">
    <div class="detail__label">ADDRESS:</div>
  </div>
  <div class="detail" style="left:368px;top:310px">
    <div class="detail__label">BASED ON</div>
    <div class="detail__value">200 GUESTS</div>
  </div>
</section>

<section class="page page--service">
  <div class="service-copy">
    <h1 class="service-copy__heading">OUR COMMITMENT<br>&amp; SERVICE TO YOU!</h1>
    <p class="service-copy__lead"><strong>Gala Works</strong> takes pride in<br>providing superior quality service!</p>
    <p class="service-copy__body">You are our guests and we take that responsibility seriously. All Gala Works’ team members are service-oriented, conscientious professionals. You can expect friendly smiles, positive communication and a staff who is happy and honored to serve you! We carefully plan and customize corporate events with attention to every detail. We value professionalism and we make you our top priority.</p>
    <h2 class="service-copy__subheading">What to Expect</h2>
    <p class="service-copy__body service-copy__body--expect">Assistance booking suppliers, vendors and services on and off site. Full coordination of your event from the first inquiry to the final departure. Unlimited communication throughout the planning process.</p>
  </div>
  <div class="service-copy__web">www.galaworks.com</div>

  <div class="service-panel">
    <div class="service-panel__art" role="img" aria-label="Flat illustration of a planning team working with charts, gears, a magnifier and a laptop"></div>
  </div>
</section>

</body>
</html>
```